Fresh Tarrow Work Post - Business Card Required

Dear All,

I own Velmira Limited, which in turn owns the website:
www.harbinworkpost.example

I want all of you wonderful creative people to come up with a slick, and awesome business card design that incorporates the logo on the site, and some colouring and design elements from it.

You have free reign in how you go about doing this, I won't be giving my contact details on this platform, but the winner will be asked to redesign based on my contact details which I will supply at the end.

I need the design to be completed within 5 days. I need the final print copies of the business cards by the 25th November, so unfortunately it's a bit of a rush to get these designs ready.

Any questions, please ask.

Thank you
Updates

Thank you all for your hard work and exceptional designs provided. I do have to pick one, so I have a very clear idea of which one this is, however I will wait one further day until the competition closes to be fair to all those have submitted, or are in the process of submitting. I wish you all the best and thank you again for your dedication.

```html
<!DOCTYPE html>
<html lang="en">
<head>
<meta charset="utf-8">
<title>Harbin Work Post — Business Card</title>
<link rel="stylesheet" href="https://fonts.googleapis.com/css2?family=Marcellus&display=swap">
<style>
  :root {
    --page-bg: #ecebe7;
    --card-black: #141414;
    --card-black-edge: #1d1d1d;
    --side-grey: #dfe0e4;
    --gold: #c9a23a;
    --gold-light: #e8cf6e;
    --panel-top: #ecdd7c;
    --panel-bottom: #fdf8e6;
    --tab-brown: #a8700e;
    --ink: #1a1a1a;
    --ink-soft: #3a3320;
    --swatch-1: #8a4707;
    --swatch-2: #b27a0e;
    --swatch-3: #dcc152;
    --swatch-4: #f6ef9a;
  }
  * { box-sizing: border-box; margin: 0; padding: 0; }
  html, body { width: 1200px; height: 1000px; overflow: hidden; }
  body {
    background: var(--page-bg);
    font-family: "Marcellus", serif;
    position: relative;
  }
  .card {
    position: absolute;
    left: 220px;
    width: 760px;
    height: 430px;
    border-radius: 4px;
    box-shadow: 0 10px 28px rgba(0,0,0,.22);
    overflow: hidden;
  }
  /* Front */
  .card--front {
    top: 50px;
    background: linear-gradient(135deg, var(--card-black-edge), var(--card-black));
  }
  .brand {
    position: absolute;
    left: 40px;
    top: 190px;
    width: 340px;
    text-align: center;
    color: var(--gold);
    font-size: 30px;
    letter-spacing: 3px;
  }
  .contact-panel {
    position: absolute;
    left: 415px;
    top: 30px;
    width: 320px;
    height: 370px;
    border-radius: 14px;
    background: linear-gradient(180deg, var(--panel-top), var(--panel-bottom) 70%);
  }
  .contact-panel::before {
    content: "";
    position: absolute;
    left: -18px;
    top: 178px;
    border-top: 20px solid transparent;
    border-bottom: 20px solid transparent;
    border-right: 18px solid #f6eeb8;
  }
  .person-name {
    position: absolute;
    left: 58px; top: 66px;
    font-size: 30px;
    color: var(--ink);
    letter-spacing: .5px;
  }
  .person-role {
    position: absolute;
    left: 64px; top: 102px;
    font-size: 15px;
    color: var(--ink-soft);
    letter-spacing: 1px;
  }
  .contact-list {
    position: absolute;
    left: 70px; top: 145px;
    list-style: none;
  }
  .contact-item {
    display: flex;
    align-items: center;
    height: 42px;
    margin-bottom: 2px;
    font-size: 15px;
    color: var(--ink);
  }
  .contact-item--address { font-size: 13px; line-height: 1.35; }
  .contact-tab {
    width: 22px; height: 22px;
    background: var(--tab-brown);
    margin-right: -4px;
  }
  .contact-icon {
    width: 30px; height: 30px;
    border-radius: 50%;
    background: var(--panel-bottom);
    border: 3px solid var(--gold-light);
    display: flex; align-items: center; justify-content: center;
    margin-right: 10px;
  }
  .contact-icon svg { width: 15px; height: 15px; fill: var(--ink); }
  /* Back */
  .card--back {
    top: 520px;
    background: var(--side-grey);
  }
  .back-field {
    position: absolute;
    left: 90px; right: 90px; top: 0; bottom: 0;
    background: var(--card-black);
  }
  .swatch-strip {
    position: absolute;
    top: 55px;
    width: 62px;
    height: 320px;
    display: flex;
    flex-direction: column;
  }
  .swatch-strip--left { left: 62px; }
  .swatch-strip--right { right: 62px; flex-direction: column-reverse; }
  .swatch { flex: 1; }
  .swatch--1 { background: var(--swatch-1); }
  .swatch--2 { background: var(--swatch-2); }
  .swatch--3 { background: var(--swatch-3); }
  .swatch--4 { background: var(--swatch-4); }
  .brand--back {
    left: 0; width: 760px;
    top: 194px;
    font-size: 36px;
  }
</style>
</head>
<body>
  <section class="card card--front" aria-label="Business card front">
    <p class="brand">HARBIN WORK POST</p>
    <div class="contact-panel">
      <h1 class="person-name">YOUR NAME</h1>
      <p class="person-role">DESIGNATION</p>
      <ul class="contact-list">
        <li class="contact-item">
          <span class="contact-tab"></span>
          <span class="contact-icon"><svg viewBox="0 0 16 16"><path d="M2 5c0-2 2-3 6-3s6 1 6 3v1h-3V5H5v1H2zM4 7h8l2 6H2zM8 8.5a2 2 0 100 4 2 2 0 000-4z"/></svg></span>
          000 . 1234 .5678
        </li>
        <li class="contact-item">
          <span class="contact-tab"></span>
          <span class="contact-icon"><svg viewBox="0 0 16 16"><path d="M1 3h14v10H1zM2 4l6 5 6-5v1L8 10 2 5z" fill-rule="evenodd"/></svg></span>
          name@email.com
        </li>
        <li class="contact-item">
          <span class="contact-tab"></span>
          <span class="contact-icon"><svg viewBox="0 0 16 16"><path d="M8 1a7 7 0 100 14A7 7 0 008 1zm0 1.5c.8 0 1.8 1.8 2 4.5H6c.2-2.7 1.2-4.5 2-4.5zM2.6 7h2.3c.1-1.7.5-3.1 1-4A5.6 5.6 0 002.6 7zm7.5-4c.5.9.9 2.3 1 4h2.3a5.6 5.6 0 00-3.3-4zM2.6 9a5.6 5.6 0 003.3 4c-.5-.9-.9-2.3-1-4zm3.4 0c.2 2.7 1.2 4.5 2 4.5s1.8-1.8 2-4.5zm5.1 0c-.1 1.7-.5 3.1-1 4a5.6 5.6 0 003.3-4z"/></svg></span>
          mywebsite.com
        </li>
        <li class="contact-item contact-item--address">
          <span class="contact-tab"></span>
          <span class="contact-icon"><svg viewBox="0 0 16 16"><path d="M8 1l7 6.5h-2V15H9.5v-4h-3v4H3V7.5H1z"/></svg></span>
          <span>123 ABC Avenue<br>ROAD 54321</span>
        </li>
      </ul>
    </div>
  </section>

  <section class="card card--back" aria-label="Business card back">
    <div class="back-field"></div>
    <div class="swatch-strip swatch-strip--left">
      <span class="swatch swatch--1"></span>
      <span class="swatch swatch--2"></span>
      <span class="swatch swatch--3"></span>
      <span class="swatch swatch--4"></span>
    </div>
    <div class="swatch-strip swatch-strip--right">
      <span class="swatch swatch--1"></span>
      <span class="swatch swatch--2"></span>
      <span class="swatch swatch--3"></span>
      <span class="swatch swatch--4"></span>
    </div>
    <p class="brand brand--back">HARBIN WORK POST</p>
  </section>
</body>
</html>
```